Keepers of the Salt Roads book cover

My goal is to choose a submission ready cover for my self-published book. I am looking for an illustrative design that coordinates with the mood of the book, and with current market expectations.

Attached for context are three prior drafts of the cover. My desire is for something more illustrative (like the first one) than obvious AI, like the other two. The story takes place in a fictional town in the Arizona desert. The landscape is a big part of the story. So I would like the mood and color palette to reflect the desert. Reflect; not be a photorealistic depiction of desert. It need not portray the desert explicitly at all, if the design can invoke it. The book does have a fantasy story, but I do not want a "fantasy book" cover. Something more contemporary in design and font choices.

For example, this cover invokes the sea: https://www.bookvarnel.example/item/47213

This one invokes a forest at night: https://www.bookvarnel.example/item/58324

And this one a different take on the sea: https://www.bookvarnel.example/item/69435

(By the way, my book with its current cover, which I hate, is at:)
https://www.bookvarnel.example/item/70546

Target Market(s)

25-80 year old, professional females.

Font styles to use
Other font styles liked:
• For the Author Name, use upper and lower case (i.e., Dale Worthen), with Abadi font, if possible. In the title, make "of the" lower case.

Requirements
Must have
• Copper Wren logo on the spine, with the words "Copper Wren" beneath it.

```html
<!DOCTYPE html>
<html lang="en">
<head>
<meta charset="utf-8">
<title>Keepers of the Salt Roads — Full Cover</title>
<link rel="stylesheet" href="https://fonts.googleapis.com/css2?family=Barlow+Condensed:wght@800&family=Montserrat:wght@500&family=Poppins:wght@400;700&family=Mulish:wght@700&display=swap">
<style>
  :root {
    --stage: #a9a9ab;
    --umber-deep: #2f1813;
    --umber: #4a261c;
    --umber-mid: #5c3023;
    --spine: #2a1510;
    --ink: #2b140e;
    --white: #ffffff;
    --photo: #8d8d8d;
  }
  * { margin: 0; padding: 0; box-sizing: border-box; }
  html, body { width: 1200px; height: 1200px; overflow: hidden; background: var(--stage); }
  .canvas { position: relative; width: 1200px; height: 1200px; }

  .cover {
    position: absolute; left: 29px; top: 188px; width: 1142px; height: 824px;
    display: flex;
  }

  /* Back cover */
  .back {
    position: relative; width: 551px; height: 100%;
    background: linear-gradient(180deg, var(--umber) 0%, var(--umber-mid) 30%, var(--umber) 55%, var(--umber-mid) 80%, var(--umber-deep) 100%);
    color: var(--white);
    font-family: "Poppins", sans-serif;
    overflow: hidden;
  }
  .back-bands { position: absolute; inset: 0; }
  .blurb {
    position: absolute; left: 29px; top: 30px; width: 505px;
    font-size: 15.2px; line-height: 18px; letter-spacing: -0.15px;
  }
  .blurb p + p { margin-top: 17px; }
  .about {
    position: absolute; left: 31px; top: 542px; width: 495px;
    display: flex; gap: 14px;
  }
  .author-photo {
    flex: none; width: 78px; height: 115px; margin-top: -2px;
    background: linear-gradient(160deg, #b9b9b9, var(--photo) 60%, #6f6f6f);
    border: 1px solid #d0d0d0;
  }
  .about p { font-size: 15.2px; line-height: 18px; letter-spacing: -0.15px; }
  .barcode-space {
    position: absolute; left: 345px; top: 684px; width: 178px; height: 106px;
    background: var(--white);
  }

  /* Spine */
  .spine {
    position: relative; width: 40px; height: 100%; background: var(--spine); color: var(--white);
  }
  .spine-title, .spine-author {
    position: absolute; left: 50%; writing-mode: vertical-rl; transform: translateX(-50%);
    white-space: nowrap;
  }
  .spine-title { top: 44px; font-family: "Barlow Condensed", sans-serif; font-weight: 800; font-size: 22px; letter-spacing: 2.4px; }
  .spine-author { top: 604px; font-family: "Mulish", sans-serif; font-weight: 700; font-size: 22px; letter-spacing: 3px; }
  .publisher {
    position: absolute; top: 446px; left: 0; width: 40px; text-align: center;
  }
  .publisher-mark { display: block; width: 30px; height: 30px; margin: 0 auto; border: 2px solid var(--white); border-radius: 50%; }
  .publisher-name { display: block; margin-top: 3px; font-family: "Poppins", sans-serif; font-weight: 400; font-size: 6px; white-space: nowrap; }

  /* Front cover */
  .front { position: relative; width: 551px; height: 100%; overflow: hidden; background: #c8693f; }
  .front svg { position: absolute; inset: 0; }
  .author-name {
    position: absolute; left: 0; right: 0; top: 734px; text-align: center;
    font-family: "Mulish", sans-serif; font-weight: 700; font-size: 44px; letter-spacing: 3px; color: var(--ink);
  }
</style>
</head>
<body>
<div class="canvas">
  <div class="cover">

    <section class="back">
      <svg class="back-bands" width="551" height="824" viewBox="0 0 551 824" aria-hidden="true">
        <path d="M0 250 C150 235 320 270 551 245 L551 300 C330 320 160 285 0 305Z" fill="#6b3a2a" opacity="0.35"/>
        <path d="M0 470 C160 455 330 490 551 465 L551 520 C330 540 170 505 0 525Z" fill="#6e3b29" opacity="0.3"/>
        <path d="M0 640 C180 625 340 655 551 635 L551 700 C340 715 170 690 0 705Z" fill="#2a140f" opacity="0.4"/>
      </svg>
      <div class="blurb">
        <p>Lucas Grant, a sharp-minded but skeptical scientist, arrives in Redstone, Arizona, with one goal: to debunk the age-old myths surrounding ley lines. But what begins as a methodical investigation into unexplained energy readings quickly spirals into a journey fraught with mystery, danger, and an unsettling clash between science and the unexplainable.</p>
        <p>As Lucas uncovers bizarre data he can’t rationalize, his path crosses with Sierra Castillo, a fiercely independent artist who draws her strength from the desert’s ancient rhythms. Deeply connected to the land and its hidden energies, Sierra’s insights defy Lucas’s logic and force him to confront truths far older—and more powerful—than anything in his textbooks.</p>
        <p>Together, they delve into the ley lines’ enigmatic power, uncovering a story woven with mystic lore, ecological activism, and a battle for the heart of a community threatened by corporate greed. As the pulse of the Earth calls to Lucas, he must decide: will he cling to the safety of skepticism, or embrace the wonder and responsibility of a force that could rewrite everything he thought he knew?</p>
        <p>With breathtaking desert landscapes, unforgettable characters, and a seamless blend of science and magic, Keepers of the Salt Roads invites readers on an exhilarating quest for truth. Can Lucas and Sierra save Redstone’s future—or will the ley lines’ secrets remain buried forever?</p>
      </div>
      <div class="about">
        <div class="author-photo" role="img" aria-label="Author portrait photograph"></div>
        <p>Dale Worthen, a native of Utah, weaves themes of mysticism, cultural heritage, and the wonders of the American West into his novels. Influenced by a love of storytelling, faith, and the great outdoors, Dale's work explores profound human connections through captivating characters and richly detailed settings.</p>
      </div>
      <div class="barcode-space"></div>
    </section>

    <section class="spine">
      <div class="spine-title">KEEPERS OF THE SALT ROADS</div>
      <div class="publisher">
        <span class="publisher-mark"></span>
        <span class="publisher-name">Copper Wren</span>
      </div>
      <div class="spine-author">Dale Worthen</div>
    </section>

    <section class="front">
      <svg width="551" height="824" viewBox="0 0 551 824">
        <g class="wash-bands" aria-hidden="true">
          <rect width="551" height="824" fill="#c8693f"/>
          <path d="M0 0 H551 V40 C400 50 200 30 0 45Z" fill="#5a2a1c"/>
          <path d="M0 45 C200 30 400 50 551 40 V95 C380 110 180 80 0 100Z" fill="#e8b98a"/>
          <path d="M0 100 C180 80 380 110 551 95 V150 C370 165 170 140 0 160Z" fill="#d48a5c"/>
          <path d="M0 160 C170 140 370 165 551 150 V215 C380 230 180 200 0 220Z" fill="#f0cfa3"/>
          <path d="M0 220 C180 200 380 230 551 215 V280 C360 300 170 265 0 290Z" fill="#b5532f"/>
          <path d="M0 290 C170 265 360 300 551 280 V350 C380 365 190 335 0 355Z" fill="#cf7a4a"/>
          <path d="M0 355 C190 335 380 365 551 350 V420 C370 440 180 405 0 425Z" fill="#a8482a"/>
          <path d="M0 425 C180 405 370 440 551 420 V500 C380 515 190 480 0 505Z" fill="#c4683f"/>
          <path d="M0 505 C190 480 380 515 551 500 V580 C360 600 170 565 0 590Z" fill="#b0572f"/>
          <path d="M0 590 C170 565 360 600 551 580 V650 C380 665 200 630 0 655Z" fill="#e3ac7d"/>
          <path d="M0 655 C200 630 380 665 551 650 V720 C370 740 180 705 0 725Z" fill="#d08a5e"/>
          <path d="M0 725 C180 705 370 740 551 720 V780 C380 795 190 770 0 785Z" fill="#e8bb8e"/>
          <path d="M0 785 C190 770 380 795 551 780 V824 H0Z" fill="#b95e36"/>
        </g>
        <g class="title">
          <text x="274" y="142" text-anchor="middle" textLength="462" lengthAdjust="spacingAndGlyphs" font-family="Barlow Condensed, sans-serif" font-weight="800" font-size="100" fill="#2b140e">KEEPERS</text>
          <text x="270" y="212" text-anchor="middle" font-family="Montserrat, sans-serif" font-weight="500" font-size="70" fill="#2b140e">of the</text>
          <text x="272" y="452" text-anchor="middle" textLength="410" lengthAdjust="spacingAndGlyphs" font-family="Poppins, sans-serif" font-weight="700" font-size="290" fill="#ffffff">SALT</text>
          <text x="272" y="605" text-anchor="middle" textLength="396" lengthAdjust="spacingAndGlyphs" font-family="Poppins, sans-serif" font-weight="700" font-size="178" fill="#ffffff">ROADS</text>
        </g>
      </svg>
      <div class="author-name">Dale Worthen</div>
    </section>

  </div>
</div>
</body>
</html>
```